Up and coming Australian Systems Integrator needs a proposal template refresh

We need to update our proposal template and are looking for a fresh, modern, simple and elegant proposal template. We'd like to keep our existing logos if possible.
NovaLink is a privately owned company operating since 2006. Offices and technical staff located in Quarry Bay and Bendigo
Sustained, profitable growth year on year
Velnet strategic partner
Velnet Advanced Enterprise Network Architecture Specialisation
Velnet Advanced Security Architecture Specialisation
Velnet Advanced Collaboration Architecture Specialisation
Velnet Advanced Unified Computing Technology Specialisation
Velnet Advanced Data Centre Architecture Specialisation (in progress)
Velnet Gold Partner – Expect 2H2018
As well as being a Velnet partner we have a well established stable of other vendors such as Brakwell, Tavrimo, Harbourtone, DPQ, Moltrane Dialogic, Zell, SkyTrover, VoLERNA Drift)
We are a top two provider of Velnet product/services in the Victorian healthcare sector.
Updates
Please feel free to use different colors and fonts as we feel the existing ones look dated.

```html
<!DOCTYPE html>
<html lang="en">
<head>
<meta charset="utf-8">
<title>NovaLink Proposal Template</title>
<link rel="stylesheet" href="https://fonts.googleapis.com/css2?family=Exo+2:wght@300&family=Open+Sans:wght@400;700&family=Roboto+Condensed:wght@400&display=swap">
<style>
  :root {
    --backdrop: #595959;
    --brand-blue: #0a4f92;
    --brand-navy: #0c2d55;
    --header-blue: #0d4a96;
    --header-deep: #0a3a7c;
    --accent-cyan: #2fd3da;
    --rule-blue: #1b4a9c;
    --heading-grey: #6a6a6a;
    --footer-grey: #8c8c8c;
    --paper: #ffffff;
  }
  * { margin: 0; padding: 0; box-sizing: border-box; }
  html, body { width: 1200px; height: 1200px; overflow: hidden; background: var(--backdrop); }
  .canvas { position: relative; width: 1200px; height: 1200px; }

  .page { position: absolute; top: 201px; width: 527px; height: 739px; overflow: hidden; background: var(--paper); }
  .page--cover { left: 66px; }
  .page--control { left: 614px; }

  .cover-shapes, .cover-photo { position: absolute; inset: 0; }

  .wordmark {
    position: absolute; font-family: "Exo 2", sans-serif; font-weight: 300;
    color: var(--paper); letter-spacing: 2px; display: flex; align-items: center; gap: 10px;
  }
  .wordmark__square { width: 22px; height: 22px; background: var(--paper); }
  .page--cover .wordmark { left: 42px; top: 66px; font-size: 30px; }
  .page--control .wordmark { left: 0; right: 0; top: 38px; justify-content: center; font-size: 36px; }

  .cover-title {
    position: absolute; left: 22px; top: 552px;
    font-family: "Open Sans", sans-serif; font-weight: 700; font-size: 32px; color: var(--accent-cyan);
  }
  .cover-date {
    position: absolute; left: 23px; top: 600px;
    font-family: "Open Sans", sans-serif; font-weight: 700; font-size: 20px; color: var(--paper);
  }
  .contact {
    position: absolute; left: 22px; font-family: "Roboto Condensed", sans-serif;
    font-size: 10.5px; line-height: 12.5px; color: var(--paper);
  }
  .contact__row { display: flex; align-items: flex-start; gap: 6px; }
  .contact__icon { width: 10px; height: 10px; flex: none; margin-top: 1px; }
  .contact--address { top: 640px; }
  .contact--phone { top: 683px; }
  .contact--email { top: 683px; left: 156px; }
  .contact--web { top: 700px; }
  .contact--abn { top: 719px; font-size: 8.5px; }

  .control-header {
    position: absolute; left: 0; top: 0; width: 100%; height: 138px;
    background: linear-gradient(180deg, var(--header-deep), var(--header-blue) 55%, #1559ab);
  }
  .section-title {
    position: absolute; left: 22px; font-family: "Open Sans", sans-serif; font-weight: 700;
    font-size: 19px; color: var(--heading-grey); letter-spacing: 0.2px;
  }
  .register {
    position: absolute; left: 22px; width: 482px; border-collapse: collapse;
    font-family: "Open Sans", sans-serif; table-layout: fixed;
  }
  .register th, .register td { border: 2px solid var(--rule-blue); height: 25.6px; }
  .register th {
    text-align: left; padding-left: 9px; font-size: 13px; font-weight: 700; color: var(--header-blue);
  }
  .register--definitions th { font-size: 15px; }

  .control-footer {
    position: absolute; left: 0; bottom: 0; width: 100%; height: 57px; background: var(--footer-grey);
    display: flex; align-items: center; justify-content: center; gap: 5px;
    font-family: "Roboto Condensed", sans-serif; font-size: 10.5px; color: var(--paper);
  }
</style>
</head>
<body>
<div class="canvas">

  <section class="page page--cover">
    <svg class="cover-shapes" width="527" height="739" viewBox="0 0 527 739">
      <rect width="527" height="739" fill="var(--brand-blue)"/>
      <polygon points="0,370 527,739 0,739" fill="var(--brand-navy)"/>
    </svg>
    <svg class="cover-photo" width="527" height="739" viewBox="0 0 527 739" role="img" aria-label="Photo of a hand touching a glowing padlock surrounded by network and business icons">
      <defs>
        <radialGradient id="photoTone" cx="0.7" cy="0.65" r="0.6">
          <stop offset="0" stop-color="#bfe6f6"/>
          <stop offset="0.55" stop-color="#8fc9e8"/>
          <stop offset="1" stop-color="#c9def0"/>
        </radialGradient>
      </defs>
      <polygon points="527,0 0,370 527,739" fill="url(#photoTone)"/>
    </svg>

    <div class="wordmark"><span class="wordmark__square"></span>NOVALINK</div>

    <h1 class="cover-title">LOREM IPSUM</h1>
    <p class="cover-date">dd / mm /yyyy</p>

    <div class="contact contact--address">
      <div class="contact__row">
        <svg class="contact__icon" viewBox="0 0 10 10"><path d="M5 0a3.5 3.5 0 0 0-3.5 3.5C1.5 6 5 10 5 10s3.5-4 3.5-6.5A3.5 3.5 0 0 0 5 0zm0 5a1.4 1.4 0 1 1 0-2.8A1.4 1.4 0 0 1 5 5z" fill="var(--accent-cyan)"/></svg>
        <span>Level 2 18 Kestrel Street, Quarry Bay Vic 3207<br>3/42 Marlow Street, Bendigo Victoria 3550<br>PO Box 728, Bendigo Victoria 3552</span>
      </div>
    </div>
    <div class="contact contact--phone">
      <div class="contact__row">
        <svg class="contact__icon" viewBox="0 0 10 10"><circle cx="5" cy="5" r="4.3" fill="none" stroke="var(--accent-cyan)" stroke-width="1"/><path d="M3.4 3c.3 1.8 1.6 3.3 3.4 3.8l.5-.8-.9-.5-.4.4C5 5.5 4.6 5 4.4 4.3l.4-.4-.5-.9z" fill="var(--accent-cyan)"/></svg>
        <span>1800 562 314</span>
      </div>
    </div>
    <div class="contact contact--email">
      <div class="contact__row">
        <svg class="contact__icon" viewBox="0 0 10 10"><rect x="0.5" y="2" width="9" height="6" fill="var(--accent-cyan)"/><path d="M0.5 2 5 5.5 9.5 2" fill="none" stroke="var(--brand-navy)" stroke-width="0.8"/></svg>
        <span>Info@NovaLink.net.au</span>
      </div>
    </div>
    <div class="contact contact--web">
      <div class="contact__row">
        <svg class="contact__icon" viewBox="0 0 10 10"><g fill="none" stroke="var(--accent-cyan)" stroke-width="0.9"><circle cx="5" cy="5" r="4.2"/><ellipse cx="5" cy="5" rx="1.8" ry="4.2"/><path d="M0.8 5h8.4"/></g></svg>
        <span>www.NovaLink.net.au</span>
      </div>
    </div>
    <div class="contact contact--abn">ABN 57 308 641 920</div>
  </section>

  <section class="page page--control">
    <header class="control-header">
      <div class="wordmark"><span class="wordmark__square"></span>NOVALINK</div>
    </header>

    <h2 class="section-title" style="top:146px">DOCUMENT CONTROL</h2>
    <table class="register" style="top:173px">
      <colgroup><col style="width:81px"><col style="width:95px"><col style="width:139px"><col style="width:167px"></colgroup>
      <tr><th>Version</th><th>Author</th><th>Description</th><th>Approval</th></tr>
      <tr><td></td><td></td><td></td><td></td></tr>
      <tr><td></td><td></td><td></td><td></td></tr>
      <tr><td></td><td></td><td></td><td></td></tr>
      <tr><td></td><td></td><td></td><td></td></tr>
    </table>

    <h2 class="section-title" style="top:322px">DISTRIBUTION LIST</h2>
    <table class="register" style="top:350px">
      <colgroup><col style="width:153px"><col style="width:162px"><col style="width:167px"></colgroup>
      <tr><th>Name</th><th>Company</th><th>Role</th></tr>
      <tr><td></td><td></td><td></td></tr>
      <tr><td></td><td></td><td></td></tr>
      <tr><td></td><td></td><td></td></tr>
      <tr><td></td><td></td><td></td></tr>
    </table>

    <h2 class="section-title" style="top:502px">DEFINITIONS</h2>
    <table class="register register--definitions" style="top:531px">
      <colgroup><col style="width:168px"><col style="width:314px"></colgroup>
      <tr><th>Term</th><th>Definitions</th></tr>
      <tr><td></td><td></td></tr>
      <tr><td></td><td></td></tr>
      <tr><td></td><td></td></tr>
      <tr><td></td><td></td></tr>
    </table>

    <footer class="control-footer">
      <svg width="10" height="10" viewBox="0 0 10 10"><g fill="none" stroke="var(--header-blue)" stroke-width="0.9"><circle cx="5" cy="5" r="4.2"/><ellipse cx="5" cy="5" rx="1.8" ry="4.2"/><path d="M0.8 5h8.4"/></g></svg>
      <span>www.NovaLink.net.au</span>
    </footer>
  </section>

</div>
</body>
</html>
```